Business Card Design Project

I need a new business card design for my building/development company: Kestrel Ridge Builders.

We specialise in small sub-divisions, multi-story developments and new house builds.
We handle the whole process from concept stage right throught to a fully developed property.
Updates

Target Market(s)

people looking to develop their property and need help. New property buyers

Industry/Entity Type

House

Requirements
Must have
• My logo on both sides:
Side 1: Logo taking up whole side as per old card but with a color/style change.

Side 2: Contact page: include logo but the rest just surprise me!

All contact details will be: (and need to be changable for each employee) I'll inform you of specifics before printing.

Name Surname
Position ie. Managing director
M: insert mobile
E: insert email
P.O. Box 518, Ashwell, Vic, 3094
www.kestrelridgebuilders.com.au

Nice to have
• Colors i'd like: (not necessarily all but this is the basic idea)

Black, blue, grey, silver, white

```html
<!DOCTYPE html>
<html lang="en">
<head>
<meta charset="utf-8">
<title>Kestrel Ridge Builders – Business Card</title>
<link rel="stylesheet" href="https://fonts.googleapis.com/css2?family=Source+Sans+3:wght@400;600;700&display=swap">
<style>
  :root {
    --page: #ffffff;
    --card: #231f20;
    --guide: #6d6a6a;
    --tab: #5b5859;
    --tab-edge: #8a8788;
    --white: #ffffff;
    --muted: #b9b7b7;
    --label: #333333;
    --brand: #ffffff;
  }
  * { margin: 0; padding: 0; box-sizing: border-box; }
  html, body {
    width: 1200px; height: 456px; overflow: hidden;
    background: var(--page);
    font-family: "Source Sans 3", "Myriad Pro", Arial, sans-serif;
  }
  .sheet { position: relative; width: 1200px; height: 456px; }
  .side-label {
    position: absolute; top: 14px; width: 120px; margin-left: -60px;
    text-align: center; font-size: 22px; color: var(--label); font-weight: 400;
  }
  .card {
    position: absolute; top: 49px; width: 555px; height: 349px;
    background: var(--card); overflow: hidden;
  }
  .card--front { left: 20px; }
  .card--back { left: 614px; }
  .guides { position: absolute; inset: 0; }
  .brand-name {
    position: absolute; white-space: nowrap; color: var(--brand);
    font-weight: 600; letter-spacing: -0.5px;
  }
  .tagline {
    position: absolute; white-space: nowrap; color: var(--white);
    font-weight: 400; letter-spacing: 0.4px;
  }
  .card--front .brand-name {
    left: 0; right: 0; text-align: center; top: 196px; font-size: 42px; line-height: 1;
  }
  .card--front .tagline {
    left: 0; right: 0; text-align: center; top: 244px; font-size: 17px;
  }
  .brand-mark {
    position: absolute; background: #1a78c2;
  }
  .card--front .brand-mark { left: 262px; top: 132px; width: 32px; height: 32px; }
  .card--back .brand-name { left: 58px; top: 131px; font-size: 25px; line-height: 1; }
  .card--back .tagline { left: 68px; top: 158px; font-size: 10.5px; }
  .person {
    position: absolute; right: 47px; top: 44px; text-align: right; color: var(--white);
  }
  .person__name { font-size: 21px; font-weight: 700; line-height: 1.1; }
  .person__role { font-size: 15px; color: var(--muted); margin-top: 3px; }
  .person__mobile { font-size: 13.5px; margin-top: 15px; }
  .contact {
    position: absolute; right: 47px; top: 243px; text-align: right;
    color: var(--white); font-size: 13px; line-height: 18.5px;
  }
</style>
</head>
<body>
<div class="sheet">
  <div class="side-label" style="left:297px">Front</div>
  <div class="side-label" style="left:890px">Back</div>

  <section class="card card--front">
    <svg class="guides" width="555" height="349" viewBox="0 0 555 349" aria-hidden="true">
      <line x1="34.5" y1="0" x2="34.5" y2="349" stroke="var(--guide)" stroke-width="1"/>
      <line x1="0" y1="297.5" x2="555" y2="297.5" stroke="var(--guide)" stroke-width="1"/>
      <circle cx="34.5" cy="297.5" r="4.5" fill="none" stroke="var(--guide)"/>
      <rect x="0.5" y="59.5" width="28" height="231" fill="var(--tab)" stroke="var(--tab-edge)"/>
    </svg>
    <div class="brand-mark" aria-hidden="true"></div>
    <div class="brand-name">Kestrel Ridge Builders</div>
    <div class="tagline">renovation-construction-development</div>
  </section>

  <section class="card card--back">
    <svg class="guides" width="555" height="349" viewBox="0 0 555 349" aria-hidden="true">
      <line x1="33.5" y1="0" x2="33.5" y2="349" stroke="var(--guide)"/>
      <line x1="517.5" y1="0" x2="517.5" y2="349" stroke="var(--guide)"/>
      <line x1="0" y1="230.5" x2="555" y2="230.5" stroke="var(--guide)"/>
      <line x1="369" y1="91.5" x2="555" y2="91.5" stroke="var(--guide)"/>
      <circle cx="33.5" cy="230.5" r="4.5" fill="none" stroke="var(--guide)"/>
      <circle cx="517.5" cy="230.5" r="4.5" fill="none" stroke="var(--guide)"/>
      <circle cx="517.5" cy="91.5" r="4.5" fill="none" stroke="var(--guide)"/>
      <rect x="525.5" y="99.5" width="29" height="124" fill="var(--tab)" stroke="var(--tab-edge)"/>
    </svg>
    <div class="brand-name">Kestrel Ridge Builders</div>
    <div class="tagline">renovation-construction-development</div>

    <div class="person">
      <div class="person__name">Marcus Hale</div>
      <div class="person__role">Managing director</div>
      <div class="person__mobile">Mobile :&nbsp; 0412 555 907</div>
    </div>

    <address class="contact" style="font-style:normal">
      Ph/Fax :&nbsp; 08 5550 2468<br>
      P.O. Box 518, Ashwell, Vic, 3094<br>
      www.kestrelridgebuilders.com.au<br>
      Email: office@kestrelridgebuilders.com.au
    </address>
  </section>
</div>
</body>
</html>
```